Brochure Design Project for Building Designer

I need a modern and edgy brochure to introduce my new business LURO Design, Commercial and Residential Building Designers.

We specialise in Building Design, Project Management and Design Consultation.

I would like the brochure to be anywhere between 2-4 pages, depending of amount of suitable content available.
Colours to be black and white with splashes of
bright colours (mostly incorporated in photos).

Main Content of brochure to be broken up into 3 (maybe 4) sections to include:

About Us
Services
Projects

Logo Text (DESIGN etc) can be changed to white if suits better with black background.

Would be nice to include sketches to give it that architectural feel.

Samples and wording will be uploaded shortly
Updates

I HAVE PROVIDED A COMPLETE UPDATE OF PROJECT REQUIREMENTS INCLUDING ALL NEW UPLOADED FILES.

PLEASE REFER TO THE BROCHURE LAYOUT PDF UPLOADEDĀ FOR FULL INFORMATION ON PROJECT INCLUDING BROCHURE LAYOUT.

IF YOU HAVE ANY QUESTIONS OR REQUIRE ANY FURTHER INFORMATION, PLEASE LET ME KNOW

I HAVE ADDED FURTHER DEVELOPED PDF DOCUMENTS OF BROCHURE.

IF YOU HAVE TROUBLE OPENING THESE DOCS IN ADOBE ILLUSTRATOR THRU ADOBE BRIDGE PLEASE LET ME KNOW & I WILL UPLOAD AI FILES.

CAN YOU PLEASE FINE TUNE GRAPHICS AND WORK ON BACKGROUND

Target Market(s)

Builders, Property Developers, Architects, Consultants, Professionals

Industry/Entity Type

Business

Requirements
Must have
• Very Professional Look
Black and White
Simple and easy to read layout
Either A4 (if only 2 pages) or
A3 double sided with centre fold (if 4 pages)
Touch up of photos (if possible) to make them stand out of the page.
Samples of recent projects with photos
Should not have
• Any comics or similar

```html
<!DOCTYPE html>
<html lang="en">
<head>
<meta charset="utf-8">
<title>About Us, Services, Projects — Brochure Page</title>
<link rel="stylesheet" href="https://fonts.googleapis.com/css2?family=Mukta:wght@400;500&display=swap">
<style>
  :root {
    --page: #ffffff;
    --page-shade: #e9e9e9;
    --ink: #111111;
    --ink-soft: #1c1c1c;
    --frame-line: #9a9a9a;
    --panel: rgba(200, 200, 200, 0.45);
    --mark: #1a1a1a;
    --mark-grey: #6d6d6d;
    --photo-warm: #c9a97b;
    --photo-light: #efe2c9;
    --photo-dark: #3a2a1c;
  }
  * { margin: 0; padding: 0; box-sizing: border-box; }
  html, body { width: 1200px; height: 847px; overflow: hidden; background: var(--page); }
  .brochure-page {
    position: relative;
    width: 1200px;
    height: 847px;
    overflow: hidden;
    font-family: "Mukta", "Segoe UI", sans-serif;
    color: var(--ink);
    background: linear-gradient(100deg, var(--page) 48%, var(--page-shade) 100%);
  }
  .sketch-backdrop {
    position: absolute;
    left: 600px; top: 0; width: 600px; height: 847px;
    background: radial-gradient(ellipse at 75% 55%, rgba(190,190,190,0.35), rgba(255,255,255,0) 70%);
  }
  .photo-frame {
    position: absolute;
    left: 5px; top: 7px; width: 596px; height: 834px;
    border: 1px solid var(--frame-line);
    background: var(--page);
  }
  .feature-photo {
    position: absolute;
    left: 16px; top: 12px; width: 574px; height: 820px;
    background:
      linear-gradient(180deg, rgba(0,0,0,0) 55%, rgba(40,28,18,0.55) 100%),
      linear-gradient(120deg, var(--photo-light) 0%, var(--photo-warm) 45%, var(--photo-dark) 100%);
  }
  .corner-marks { position: absolute; left: 0; top: 0; width: 1200px; height: 847px; pointer-events: none; }
  .content { position: absolute; left: 617px; top: 0; width: 560px; }
  .section-title {
    font-weight: 400;
    font-size: 34px;
    letter-spacing: 1.4px;
    line-height: 1;
    position: absolute;
    left: 0;
    white-space: nowrap;
  }
  .about-title { top: 22px; }
  .body-text {
    font-size: 18px; line-height: 24.5px; letter-spacing: 0.6px;
    color: var(--ink-soft); white-space: nowrap;
  }
  .about-text { position: absolute; left: 4px; top: 70px; }
  .about-text p + p { margin-top: 24px; }
  .services-panel {
    position: absolute; left: 612px; top: 208px; width: 563px; height: 309px;
    background: var(--panel);
  }
  .services-title { left: 8px; top: 14px; }
  .services-list {
    position: absolute; left: 12px; top: 60px; width: 545px;
    list-style: none; white-space: nowrap;
    font-size: 15px; line-height: 19.5px; letter-spacing: 0.5px;
    text-transform: uppercase; color: var(--ink-soft);
  }
  .projects-title { top: 535px; }
  .projects-text { position: absolute; left: 3px; top: 598px; }
  .projects-text p + p { margin-top: 24.5px; }
</style>
</head>
<body>
<main class="brochure-page">
  <div class="sketch-backdrop" role="img" aria-label="Faint architectural sketch drawings in the background"></div>

  <div class="photo-frame"></div>
  <div class="feature-photo" role="img" aria-label="Photograph of a modern double-height interior with a floating staircase, lounge and dark dining table"></div>

  <svg class="corner-marks" viewBox="0 0 1200 847" aria-hidden="true">
    <g fill="var(--mark)">
      <rect x="49" y="0" width="5" height="11"/><rect x="58" y="0" width="5" height="11"/><rect x="67" y="0" width="5" height="11"/>
      <rect x="0" y="49" width="16" height="5"/><rect x="0" y="58" width="16" height="5"/><rect x="0" y="67" width="16" height="5"/>
      <rect x="0" y="775" width="16" height="5"/><rect x="0" y="784" width="16" height="5"/><rect x="0" y="793" width="16" height="5"/>
      <rect x="47" y="833" width="5" height="14"/><rect x="56" y="833" width="5" height="14"/><rect x="65" y="833" width="5" height="14"/>
      <rect x="1134" y="30" width="66" height="4"/>
      <rect x="1173" y="802" width="27" height="10"/>
    </g>
    <g fill="var(--mark-grey)">
      <rect x="1185" y="40" width="15" height="10"/>
      <rect x="1134" y="820" width="66" height="3"/>
    </g>
  </svg>

  <section class="content">
    <h2 class="section-title about-title">ABOUT US</h2>
    <div class="about-text body-text">
      <p>Commercial and Residential Building Designers.</p>
      <p>We specialise in Building Design, Project Management and Design<br>Consultation.</p>
    </div>
  </section>

  <section class="services-panel">
    <h2 class="section-title services-title">SERVICES</h2>
    <ul class="services-list">
      <li>We are able to provide a wide range of services including<br>the following:</li>
      <li>Project Planning</li>
      <li>Design Concepts</li>
      <li>Design Development / Development Approval</li>
      <li>Consultant Liaison + Management</li>
      <li>Building Certification</li>
      <li>Tender / Construction Documentation</li>
      <li>Project Management</li>
      <li>3D Modelling &amp; Renders</li>
      <li>Re-Documentation &amp; Design Consultation</li>
      <li>Drafting Services</li>
    </ul>
  </section>

  <section class="content">
    <h2 class="section-title projects-title">PROJECTS</h2>
    <div class="projects-text body-text">
      <p>A project in business and science is typically defined as a collabora-<br>tive enterprise, frequently involving research or design, that is care-<br>fully planned to achieve.</p>
      <p>A project in business and science is typically defined as a collabora-<br>tive enterprise, frequently involving research or design, that is care-<br>fully planned to achieve</p>
    </div>
  </section>
</main>
</body>
</html>
```